Website Design for a Project Management Consulting Business

I have a logo design already and now I need a website.
I am a project manager and run my own consulting business.
Currently I am under contract with 3 major Kestrelmark 300 companies. I'd like a website I can direct current and future clients.
My job is running IT projects and working with developers to deliver business priorities.
The website should be professional and clean - I work IT projects and would like to incorporate that into any theme.
I'd like the site to have several page or breakoff links - sections would include : about me, about my services, a page to display all of my certification badges, another page to talk about highlights from past projects and so on.
Looking for a collaborative experience.

Industry/Entity Type

Kestrelmark 300 Consulting Firm - Project Management

Coding

Coded - Design and coding required

Number of Pages Required

1 page

Font styles to use
Serif

Colors
0094D4
00A9DD
6FCCEA
C7EBF8
E9F6FB
EE7325
F08F49
F5BC92
FAE3D3
FDF4ED

Requirements
Must have
• Sections that are a must: About Me (bio), About My Services, About my Certifications and Credentials, Experience on Past Projects,
Nice to have
• I have added the logo below - I'd like to use the logo and have it prominent ; should be professional and inviting

```html
<!DOCTYPE html>
<html lang="en">
<head>
<meta charset="utf-8">
<title>Meridian Project Partners LLC</title>
<link href="https://fonts.googleapis.com/css2?family=Prompt:wght@400;500&family=Roboto:wght@400;500;700&display=swap" rel="stylesheet">
<style>
:root{
  --navy:#033766;
  --navy-deep:#022a50;
  --blue:#0094d4;
  --sky:#6fccea;
  --ink:#111b27;
  --text:#5b6470;
  --line:#0094d4;
  --white:#ffffff;
}
*{margin:0;padding:0;box-sizing:border-box}
html,body{width:1200px;height:3254px;overflow:hidden}
body{position:relative;background:var(--white);font-family:"Roboto",Arial,sans-serif;color:var(--ink)}
.abs{position:absolute}
.head{font-family:"Prompt",Arial,sans-serif;font-weight:500}

/* hero */
.hero-photo{left:634px;top:0;width:566px;height:753px;border-bottom-right-radius:230px;
  background:linear-gradient(160deg,#e9e4df 0%,#cfc3b8 35%,#6f87a6 60%,#4f6c90 100%)}
.hero-panel{left:0;top:0;width:634px;height:753px;background:var(--navy);border-bottom-right-radius:240px}
.brand{left:86px;top:18px;color:var(--white);font-family:"Prompt",sans-serif;font-weight:500;font-size:28px;letter-spacing:1px;display:flex;align-items:center;gap:10px}
.brand .mark{width:44px;height:44px;border:3px solid var(--white)}
.contact{top:22px;display:flex;gap:14px;align-items:center;font-size:15px}
.contact small{display:block;color:#6b7480;font-size:15px;margin-bottom:6px}
.contact b{font-weight:700;color:var(--navy)}
.nav{left:86px;top:90px;width:1028px;height:54px;background:var(--white);display:flex;align-items:center;font-size:13.5px}
.nav a{color:var(--ink);text-decoration:none;margin-left:32px}
.nav a.on{color:var(--blue);margin-left:37px}
.social{display:flex;gap:14px;margin-left:auto;margin-right:26px}
.dot{width:12px;height:12px;border-radius:50%;border:2px solid var(--navy)}
.cta{width:139px;height:54px;background:var(--blue);color:var(--white);display:flex;align-items:center;justify-content:center;font-size:14px}
.eyebrow{display:flex;align-items:center;gap:12px;font-family:"Prompt",sans-serif;font-size:18px}
.eyebrow::before{content:"";width:40px;height:2px;background:var(--blue)}
.hero-title{left:86px;top:296px;width:470px;color:var(--white);font-size:40px;line-height:48px}
.hero-title span{color:var(--blue)}
.hero-copy{left:86px;top:460px;width:440px;color:var(--white);font-size:15px;line-height:23px}
.btn{left:86px;top:557px;width:176px;height:54px;border-radius:27px;background:var(--blue);color:var(--white);display:flex;align-items:center;justify-content:center;font-weight:500;font-size:15px}

/* about */
.about-photo{left:615px;top:856px;width:585px;height:457px;border-top-left-radius:150px;border-bottom-right-radius:150px;
  background:linear-gradient(135deg,#c9ccd3 0%,#8f7f74 45%,#3a3f4d 100%)}
.label{color:var(--blue);font-family:"Prompt",sans-serif;font-size:17px}
.h2{font-family:"Prompt",sans-serif;font-weight:500;font-size:33px;line-height:41px;color:var(--ink)}
.about-title{left:86px;top:918px;width:520px;font-size:30px;line-height:40px;letter-spacing:-0.2px;white-space:nowrap}
.body{font-size:14px;line-height:23px;color:var(--text)}
.quote{left:86px;top:1150px;width:470px;border-left:4px solid var(--blue);padding-left:14px;font-weight:700;font-size:15px;line-height:23px}
.quote em{font-style:normal;color:var(--blue);font-weight:500}
.sig{left:84px;top:1218px;width:175px;height:50px;background:linear-gradient(90deg,#eef1f4,#f7f8fa);border-radius:4px}
.sig-name{left:285px;top:1212px;border-left:1px solid #c5ccd4;padding-left:20px;height:56px}
.sig-name b{font-family:"Prompt",sans-serif;font-weight:500;font-size:19px;display:block}
.sig-name span{color:var(--blue);font-size:14px}

/* services */
.center{left:0;width:1200px;text-align:center}
.centered-label{display:inline-flex;align-items:center;gap:12px}
.centered-label::before,.centered-label::after{content:"";width:36px;height:2px;background:var(--blue)}
.card{width:326px}
.icon{width:105px;height:105px;border-radius:50%;background:var(--blue);display:flex;align-items:center;justify-content:center}
.icon.dark{background:var(--navy)}
.card-title{position:absolute;left:128px;top:20px;font-family:"Prompt",sans-serif;font-weight:500;font-size:21px;line-height:30px;color:var(--navy)}
.card .body{margin-top:22px}
.more{display:flex;align-items:center;gap:10px;margin-top:16px;font-weight:500;font-size:15px;color:var(--navy)}
.more::after{content:"";flex:1;height:1px;background:var(--line)}

/* certifications */
.band{left:0;top:1841px;width:1200px;height:168px;background:linear-gradient(90deg,var(--navy) 0%,#1d4d80 50%,var(--navy) 100%)}
.badge{top:1884px;width:84px;height:84px}
.projects-bg{left:0;top:2009px;width:1200px;height:230px;background:var(--white);border-top-left-radius:190px}
.band-foot{left:0;top:2009px;width:200px;height:200px;background:linear-gradient(90deg,var(--navy),#1d4d80)}

/* projects */
.proj-img{top:2210px;width:326px;height:334px;border-bottom-right-radius:90px}
.proj-title{font-family:"Prompt",sans-serif;font-weight:500;font-size:21px;color:var(--navy)}
.proj-title::after{content:"";display:block;width:38px;height:2px;background:var(--blue);margin-top:14px}

/* footer */
.footer{left:0;top:2825px;width:1200px;height:343px;background:var(--navy)}
.footbar{left:0;top:3168px;width:1200px;height:86px;background:var(--navy-deep)}
.fcol h4{font-family:"Prompt",sans-serif;font-weight:500;font-size:19px;color:var(--white)}
.fcol h4::after{content:"";display:block;width:40px;height:2px;background:var(--blue);margin-top:14px}
.fcol ul{list-style:none;margin-top:18px}
.fcol li,.fcol p{color:var(--white);font-size:13.5px;line-height:36px}
.fcol p{line-height:23px;margin-top:18px}
.ring{width:31px;height:31px;border-radius:50%;border:1.5px solid var(--white)}
.flogo{left:86px;top:3136px;width:237px;height:118px;background:var(--white);clip-path:polygon(0 20%,100% 0,100% 100%,0 100%)}
.copy{right:86px;top:3200px;color:var(--white);font-size:15px}
</style>
</head>
<body>

<!-- hero -->
<div class="abs hero-photo" role="img" aria-label="Photo of the consultant in a blue plaid blazer standing in an office"></div>
<div class="abs hero-panel"></div>
<div class="abs brand"><span class="mark"></span>MERIDIAN PARTNERS</div>

<div class="abs contact" style="left:680px">
  <svg width="44" height="44" viewBox="0 0 44 44" fill="none" stroke="#033766" stroke-width="1.6"><path d="M9 26v-6a13 13 0 0 1 26 0v6"/><rect x="6" y="24" width="7" height="11" rx="3"/><rect x="31" y="24" width="7" height="11" rx="3"/><path d="M34 35c0 4-4 5-10 5"/></svg>
  <div><small>Call</small><b>(555) 014-2290</b></div>
</div>
<div class="abs contact" style="left:872px">
  <svg width="46" height="36" viewBox="0 0 46 36" fill="none" stroke="#033766" stroke-width="1.6"><rect x="2" y="4" width="42" height="28"/><path d="M2 4l21 16 21-16M2 32l16-14M44 32L28 18"/></svg>
  <div><small>Email</small><b>hello@meridian-pm.com</b></div>
</div>

<nav class="abs nav">
  <a class="on">Home</a><a>About Me</a><a>My Services</a><a>My Certification Badges</a><a>Past Project</a>
  <div class="social"><span class="dot"></span><span class="dot"></span><span class="dot"></span></div>
  <div class="cta">Get In Touch</div>
</nav>

<div class="abs eyebrow" style="left:86px;top:253px;color:#fff">Top IT Project Manager</div>
<h1 class="abs hero-title head"><span>Welcome To</span> Meridian Project Partners LLC</h1>
<p class="abs hero-copy">Lorem ipsum dolor sit amet, consectetur adipiscing elit. Duis rhoncus sem et interdum volutpat. Lorem ipsum dolor sit amet, consectetur adipiscing elit. Praesent et arcu nibh.</p>
<div class="abs btn">Learn More</div>

<!-- about -->
<div class="abs about-photo" role="img" aria-label="Portrait of the consultant in a pinstripe jacket in front of a screen with charts"></div>
<div class="abs eyebrow label" style="left:86px;top:886px">About Me</div>
<h2 class="abs h2 about-title">I am a project manager and run<br>my own consulting business.</h2>
<p class="abs body" style="left:86px;top:1015px;width:490px">There are many variations of passages of orem Ipsum available, but the majority have suffered alteration in some form, by cted ipsum dolor sit amet, consectetur adipisicing elit, sed do usmod temponcid idunt ut labore et dolore magna aliqua. Ut enim ad minim veniam, quis nostrud exercitation ullamco aboris nisi.</p>
<p class="abs quote">Hello I am <em>Jordan Ellery.</em>Currently I am under contract with 3 major <em>Kestrelmark 300</em> companies.</p>
<div class="abs sig" role="img" aria-label="Handwritten signature"></div>
<div class="abs sig-name"><b>Jordan Ellery</b><span>Project Manager</span></div>

<!-- services -->
<div class="abs center" style="top:1412px"><span class="label centered-label">Services</span></div>
<h2 class="abs center h2" style="top:1444px">I Serve the Best Work</h2>

<div class="abs card" style="left:86px;top:1516px">
  <div class="icon"><svg width="46" height="40" viewBox="0 0 46 40" fill="none" stroke="#fff" stroke-width="2"><rect x="3" y="3" width="40" height="26"/><path d="M12 29l-5 9M34 29l5 9M11 20l8-6 7 5 10-9"/></svg></div>
  <div class="card-title">Strategy<br>and Planning</div>
  <p class="body">There are many variations of passages of orem Ipsum available, but the majority have suffered alteration in some form</p>
  <div class="more">Read More</div>
</div>
<div class="abs card" style="left:437px;top:1516px">
  <div class="icon dark"><svg width="44" height="40" viewBox="0 0 44 40" fill="none" stroke="#fff" stroke-width="2"><rect x="4" y="3" width="36" height="26"/><path d="M12 24v-6M19 24v-10M26 24v-8M33 24v-14M14 36h16"/></svg></div>
  <div class="card-title">Business<br>Analysis</div>
  <p class="body">There are many variations of passages of orem Ipsum available, but the majority have suffered alteration in some form</p>
  <div class="more">Read More</div>
</div>
<div class="abs card" style="left:789px;top:1516px">
  <div class="icon"><svg width="44" height="44" viewBox="0 0 44 44"><path d="M20 22V6a16 16 0 1 0 16 16z" fill="#fff"/><path d="M24 18V4a14 14 0 0 1 14 14z" fill="#f08f49"/><circle cx="31" cy="31" r="6" fill="none" stroke="#033766" stroke-width="2.5"/><path d="M35 35l5 5" stroke="#033766" stroke-width="3"/></svg></div>
  <div class="card-title">Market<br>Research</div>
  <p class="body">There are many variations of passages of orem Ipsum available, but the majority have suffered alteration in some form</p>
  <div class="more">Read More</div>
</div>

<!-- certifications -->
<div class="abs band"></div>
<svg class="abs badge" style="left:120px" viewBox="0 0 84 84"><path d="M42 2 82 42 42 82 2 42z" fill="#e9f6fb"/></svg>
<svg class="abs badge" style="left:295px" viewBox="0 0 84 84"><circle cx="42" cy="42" r="40" fill="#fff" stroke="#6b2d8f" stroke-width="4"/></svg>
<svg class="abs badge" style="left:471px" viewBox="0 0 84 84"><path d="M42 2 82 42 42 82 2 42z" fill="#e9f6fb"/></svg>
<svg class="abs badge" style="left:645px" viewBox="0 0 84 84"><circle cx="42" cy="42" r="40" fill="#f5bc5a"/></svg>
<svg class="abs badge" style="left:823px" viewBox="0 0 84 84"><circle cx="42" cy="42" r="40" fill="#fff" stroke="#6b2d8f" stroke-width="4"/></svg>
<svg class="abs badge" style="left:996px" viewBox="0 0 84 84"><circle cx="42" cy="42" r="40" fill="#ee7325"/></svg>
<div class="abs band-foot"></div>
<div class="abs projects-bg"></div>

<!-- projects -->
<div class="abs center" style="top:2108px"><span class="label centered-label">Projects</span></div>
<h2 class="abs center h2" style="top:2140px">My IT Projects</h2>

<div class="abs proj-img" style="left:86px;background:linear-gradient(160deg,#5a6b5c,#b9bcbf 60%,#ecedee)" role="img" aria-label="Developer typing at a desktop computer showing code"></div>
<div class="abs proj-img" style="left:437px;background:linear-gradient(160deg,#2e3640,#8a9aa8 55%,#dfe4ea)" role="img" aria-label="Team reviewing printed charts on a table"></div>
<div class="abs proj-img" style="left:788px;background:linear-gradient(160deg,#3c4658,#c4cbd6 55%,#f1f3f6)" role="img" aria-label="Colleagues pointing at colourful report graphs"></div>

<div class="abs card" style="left:86px;top:2566px"><div class="proj-title">Consulting Project</div><p class="body" style="margin-top:20px">There are many variations of passages of orem Ipsum available, but the majority have suffered alteration in some form</p><div class="more">Read More</div></div>
<div class="abs card" style="left:437px;top:2566px"><div class="proj-title">Consulting Project</div><p class="body" style="margin-top:20px">There are many variations of passages of orem Ipsum available, but the majority have suffered alteration in some form</p><div class="more">Read More</div></div>
<div class="abs card" style="left:788px;top:2566px"><div class="proj-title">Consulting Project</div><p class="body" style="margin-top:20px">There are many variations of passages of orem Ipsum available, but the majority have suffered alteration in some form</p><div class="more">Read More</div></div>

<!-- footer -->
<div class="abs footer"></div>
<svg class="abs" style="left:10px;top:2910px" width="90" height="90"><circle cx="45" cy="45" r="45" fill="#0b4a85"/></svg>
<svg class="abs" style="left:1087px;top:2851px" width="44" height="44"><circle cx="22" cy="22" r="22" fill="#0b4a85"/></svg>
<svg class="abs" style="left:1134px;top:2899px" width="22" height="22"><circle cx="11" cy="11" r="10" fill="#0094d4"/></svg>

<div class="abs fcol" style="left:86px;top:2880px;width:280px"><h4>About Me</h4><p>My job is running IT projects and working with developers to deliver business priorities.</p></div>
<div class="abs fcol" style="left:463px;top:2880px"><h4>Services</h4><ul><li>Strategy and Planning</li><li>Business Analysis</li><li>Consumer Markets</li><li>Corporate Finance</li><li>Market Research</li></ul></div>
<div class="abs fcol" style="left:701px;top:2880px"><h4>Quick Links</h4><ul><li>Home</li><li>About Me</li><li>My Services</li><li>My Certification Badges</li><li>Past Project</li></ul></div>
<div class="abs fcol" style="left:929px;top:2880px"><h4>Connect To Me</h4>
  <div style="display:flex;gap:9px;margin-top:20px"><span class="ring"></span><span class="ring"></span><span class="ring"></span></div></div>

<div class="abs footbar"></div>
<div class="abs flogo"></div>
<div class="abs" style="left:110px;top:3206px;display:flex;align-items:center;gap:8px;font-family:'Prompt',sans-serif;font-weight:500;font-size:16px;color:#033766"><span style="width:24px;height:24px;border:2px solid #033766"></span>MERIDIAN PARTNERS</div>
<div class="abs copy">@ Copyright 2022.All Right Reserved.</div>

</body>
</html>
```